Dailyvane Homepare Redesign - Morris

After scores of designs were submitted in response to our recent PixelGuild competition to re-think the Dailyvane.com homepage, we went back and looked at each of the artist’s portfolios. Several - including yours - were of particular interest to you.
We are now asking a handful of these designers to take a stab at a new Dailyvane.com homepage – again – but this time in accordance with some fresh guidelines. (See below.)
For this you will be paid $500 (US). We would need to have your work by Friday, March 4.
Furthermore, if we ask you to take your design through several additional stages, to a “final,” you will be paid an additional $750.
Please let us know as soon as possible if you are agreeable to this proposal.
What we have attached here are several wireframes that will help guide you to what we are after.
There are two wireframes, the first is that of the homepage. It has an area, at the top, that we are calling “the canvas”. The canvas will display different templates. The second wireframe features four different canvas templates.
We would like you to design one main homepage comp.
Once you are done with the homepage comp, please create 4 versions of it, each with a different canvas template in the “canvas” area.
Remember, the wireframes are for position only. Please use your creative judgment on colors, sizes, scale, styles, and graphics.
Generally speaking, it should be apparent that we seek a spare, clean look – easy to navigate, not too crowded with small images or unnecessary embellishment. Our audience tends to be older and not especially Web-savvy.
If you have any questions, do not hesitate to ask.
Will you participate in this project?

```html
<!DOCTYPE html>
<html lang="en">
<head>
<meta charset="utf-8">
<title>Dailyvane.com — Homepage</title>
<link href="https://fonts.googleapis.com/css2?family=Arimo:wght@400;700&display=swap" rel="stylesheet">
<style>
:root{
  --black:#000;
  --red:#e3170d;
  --red-light:#ff3a2a;
  --blue:#1e8fcc;
  --blue-top:#5cc6f1;
  --blue-bottom:#1a93d2;
  --text:#333;
  --muted:#555;
  --frame:#e4e8ec;
  --line:#d6d9dc;
  --white:#fff;
  --photo-a:#4a3f3a;
  --photo-b:#8a6a5a;
}
*{margin:0;padding:0;box-sizing:border-box}
html,body{width:1200px;height:900px;overflow:hidden}
body{position:relative;background:var(--white);font-family:"Arimo",Arial,sans-serif;color:var(--text)}
a{color:inherit;text-decoration:none}
.abs{position:absolute}

/* Top section bar */
.topbar{left:0;top:0;width:1200px;height:46px;background:var(--black)}
.topbar a{position:absolute;top:11px;height:22px;line-height:22px;font-size:12px;font-weight:700;color:var(--white)}
.topbar .active{background:var(--red);border-radius:3px;padding:0 14px;left:105px}

/* Header */
.header{left:0;top:46px;width:1200px;height:147px;background:linear-gradient(#fafafa,#e9e9e9 60%,#d9d9d9)}
.brand{left:105px;top:78px;font-size:50px;font-weight:700;color:var(--blue);letter-spacing:-1px;line-height:52px}
.tagline{left:323px;top:133px;font-size:12px;font-weight:700;color:#222}
.divider{left:467px;top:96px;width:1px;height:15px;background:#444}
.account{left:490px;top:90px;font-size:12px}
.account .links a{color:var(--blue);font-weight:700;text-decoration:underline}
.account .links span{color:#666;margin:0 4px}
.account .welcome{font-size:11px;color:#222;margin-top:1px}
.hot{left:683px;top:77px;font-size:11px}
.hot h4{color:var(--red);font-size:11px}
.hot p{color:#333;margin-top:3px}
.hot p span{color:#aaa;margin:0 6px}
.search{left:684px;top:111px;width:411px;height:24px;border:2px solid var(--red);background:var(--white);display:flex}
.search .field{flex:1;font-size:11px;color:#555;padding:4px 9px}
.search .go{width:63px;background:linear-gradient(var(--red-light),var(--red));color:var(--white);font-size:11px;font-weight:700;text-align:center;line-height:20px}

/* Main navigation */
.nav{left:105px;top:155px;width:990px;height:38px;background:linear-gradient(var(--blue-top),var(--blue-bottom));border-radius:4px 4px 0 0;display:flex}
.nav a{font-size:13px;font-weight:700;color:var(--white);line-height:40px;padding:0 18px;border-right:1px solid rgba(255,255,255,.35)}
.nav a.current{background:linear-gradient(var(--red-light),var(--red));width:100px;text-align:center;margin-top:-3px;line-height:44px;border-radius:4px 4px 0 0;padding:0}
.nav a:last-child{border:0}
.mustreads{left:0;top:194px;width:1200px;height:36px;background:linear-gradient(#fff,#e4e4e4);border-bottom:1px solid #ccc}
.mustreads ul{position:absolute;left:119px;top:11px;list-style:none;display:flex;font-size:11px;font-weight:700;color:#111}
.mustreads li{padding:0 10px;border-left:1px solid #ccc}
.mustreads li.label{color:#116ea8;font-size:12px;border:0;padding:0 8px 0 0}
.mustreads li:nth-child(2){border:0;padding-left:0}

/* Canvas feature */
.feature{left:105px;top:242px;width:990px;height:311px;background:var(--frame);padding:7px}
.feature .inner{background:var(--white);border:1px solid var(--line);height:100%;padding:18px 0 0 50px}
.feature h1{font-size:35px;color:var(--blue);font-weight:700;margin-left:-14px;letter-spacing:-.2px}
.feature ul{list-style:none;margin-top:13px}
.feature li{font-size:14px;line-height:24px;color:var(--text);padding-left:12px;position:relative}
.feature li::before{content:"";position:absolute;left:0;top:8px;border-left:6px solid var(--blue);border-top:4px solid transparent;border-bottom:4px solid transparent}

/* Panels */
.panel{background:var(--frame);padding:7px}
.panel-head{height:40px;background:linear-gradient(var(--blue-top),var(--blue-bottom));color:var(--white);font-size:18px;font-weight:700;line-height:42px;padding-left:14px}
.panel-body{background:var(--white);border:1px solid var(--line);border-top:0;height:100%}
.newsfront{left:105px;top:566px;width:677px;height:360px}
.story{display:flex;margin:0 16px;padding:17px 0 16px;border-bottom:1px dotted #999}
.thumb{width:74px;height:58px;flex:none;background:linear-gradient(135deg,var(--photo-b),var(--photo-a) 60%,#2a3550)}
.story .copy{margin-left:13px}
.story h3{font-size:14px;color:var(--blue);font-weight:700;margin-top:2px}
.story p{font-size:12px;line-height:18px;color:var(--muted);margin-top:2px}

/* Alerts signup */
.alerts{left:795px;top:566px;width:300px;height:179px;background:var(--red);padding:6px}
.alerts .inner{height:100%;background:linear-gradient(#ff3b2b,#f01d10);position:relative}
.alerts h2{position:absolute;left:54px;top:16px;font-size:20px;color:var(--white);font-weight:700}
.alerts svg{position:absolute;left:12px;top:12px}
.alerts label{position:absolute;width:50px;text-align:right;left:0;font-size:11px;font-weight:700;color:var(--white)}
.alerts .input{position:absolute;left:58px;width:213px;height:25px;background:var(--white);border:1px solid #bbb;font-size:11px;color:#222;padding:5px 10px}
.alerts .btn{position:absolute;left:69px;top:126px;width:72px;height:25px;border-radius:4px;background:linear-gradient(#fff,#d2d2d2);border:1px solid #999;font-size:12px;font-weight:700;color:#222;text-align:center;line-height:23px}

/* Voices */
.voices{left:795px;top:758px;width:300px;height:170px}
.voice{display:flex;margin:0 13px;padding:14px 0 13px;border-bottom:1px dotted #999}
.voice .copy{margin-left:10px}
.voice h3{font-size:12px;color:var(--blue);font-weight:700;margin-top:2px}
.voice .by{font-size:12px;color:#333;margin-top:5px}
.voice .meta{font-size:11px;color:#666;margin-top:5px;display:flex;align-items:center;gap:4px}
.voice .meta a{text-decoration:underline}
</style>
</head>
<body>

<nav class="abs topbar">
  <a class="active" href="#">MONEY</a>
  <a href="#" style="left:210px">HEALTH</a>
  <a href="#" style="left:303px">WORLD</a>
  <a href="#" style="left:397px">TV</a>
  <a href="#" style="left:462px">VOICES</a>
</nav>

<header>
  <div class="abs header"></div>
  <div class="abs brand">Dailyvane.com</div>
  <div class="abs tagline">Your Tagline Here</div>
  <div class="abs divider"></div>
  <div class="abs account">
    <div class="links"><a href="#">Sign In</a><span>|</span><a href="#">Register</a></div>
    <div class="welcome">Welcome to Dailyvane</div>
  </div>
  <div class="abs hot">
    <h4>Hot Topics:</h4>
    <p>Lorem<span>|</span>Lipsum<span>|</span>Quisque<span>|</span>Vestibulum<span>|</span>Mauris</p>
  </div>
  <form class="abs search">
    <div class="field">Enter Your Keword</div>
    <div class="go">SEARCH</div>
  </form>
  <nav class="abs nav">
    <a class="current" href="#">NewsFront</a>
    <a href="#">United States</a>
    <a href="#">Politics</a>
    <a href="#">The Wire</a>
    <a href="#">Voices</a>
    <a href="#">Fast Features</a>
    <a href="#">Technology</a>
    <a href="#">Slideshows</a>
    <a href="#">Jokes</a>
    <a href="#" style="padding-left:2px">Cartoons</a>
  </nav>
  <div class="abs mustreads">
    <ul>
      <li class="label">Must Reads:</li>
      <li>Lorem ipsum dolor sit amet</li>
      <li>Nullam molestie ligula eni</li>
      <li>Vestibulum vel vestibulum tellus</li>
      <li>Integer lacinia erat vel sapien commodo</li>
    </ul>
  </div>
</header>

<section class="abs feature">
  <div class="inner">
    <h1>Vestibulu vestibulum tellus uisque tempor commodo.</h1>
    <ul>
      <li>Pellentesque idleo that has and the waht ist hantesque idm molestie ligula eleo thleo that has and thes erat posuere tempor anthat&nbsp; anec.</li>
      <li>Nullam molestie ligula eleo thatthat ntesque idleom molestie ligula eleo thatthat ntesas att eh nh st has been quis enimel condimentum.</li>
      <li>Duis mattism molestie ligula eleo thatthat ntesque idleo that has m molestie ligula eleo thatas and the waht ist has been quis eet convallis.</li>
      <li>Pellentesque idleo that has and the wntesm molestie ligula eleo thatthat ntesque idleo thatnd theahteen quierat posuere tempor anthat&nbsp; anec.</li>
      <li>Nullam molestie ligulm molestie ligula eleo thatthat ntesqs att ehte sntesque idleo that has and thet has been quis enimel condimentum.</li>
      <li>Duis mattis iaculis eros leo thm molestie ligula eleo thatthat ntesque idleo that has idleo that has and theht ist has been quis eet convallis.</li>
      <li>Nullam mntesque idleo that has and theolestie ligula eleo thatthat has att eh nh st hasm molestie ligula eleo atthn quis enimel condimentum.</li>
      <li>Pellentesque idleo that has and the waht ist hantesque idm molestie ligula eleo thatthat ntesque idleo that has thatuere tempor anthat&nbsp; anec.</li>
      <li>Nullam mntesque idleo that has and theolestie ligula eleo thattham molestie ligula eleo thatthat ntesque idleo that hasmel condimentum.</li>
    </ul>
  </div>
</section>

<section class="abs panel newsfront">
  <div class="panel-head">NewsFront</div>
  <div class="panel-body">
    <article class="story">
      <div class="thumb" role="img" aria-label="News photo of a speaker at a podium"></div>
      <div class="copy">
        <h3>Vestibulu vestibulum tellus that hasining the bashing uisque teipor ancommodo.</h3>
        <p>Vestibulum vehicula hendrerit interdum. Pellentesque id leo quis erat posuere tempor anthat&nbsp; anec<br>nisanDuis mattis iaculis eros et convallis. Nullam molestie ligula enimel condimentum...</p>
      </div>
    </article>
    <article class="story">
      <div class="thumb" role="img" aria-label="News photo of a speaker at a podium"></div>
      <div class="copy">
        <h3>Vestibulu vestibulum tellus that hasining the bashing uisque teipor ancommodo.</h3>
        <p>Vestibulum vehicula hendrerit interdum. Pellentesque id leo quis erat posuere tempor anthat&nbsp; anec<br>nisanDuis mattis iaculis eros et convallis. Nullam molestie ligula enimel condimentum...</p>
      </div>
    </article>
    <article class="story">
      <div class="thumb" role="img" aria-label="News photo of a speaker at a podium"></div>
      <div class="copy">
        <h3>Vestibulu vestibulum tellus that hasining the bashing uisque teipor ancommodo.</h3>
        <p>Vestibulum vehicula hendrerit interdum. Pellentesque id leo quis erat posuere tempor anthat&nbsp; anec<br>nisanDuis mattis iaculis eros et convallis. Nullam molestie ligula enimel condimentum...</p>
      </div>
    </article>
  </div>
</section>

<aside class="abs alerts">
  <div class="inner">
    <svg width="34" height="22" viewBox="0 0 34 22" aria-hidden="true">
      <rect x="1" y="1" width="32" height="20" fill="#ffd84a" stroke="#c99a10"/>
      <path d="M1 1 L17 13 L33 1" fill="none" stroke="#c99a10" stroke-width="1.5"/>
    </svg>
    <h2>Sign up for News Alerts</h2>
    <label style="top:63px">Email:</label>
    <div class="input" style="top:57px">Enter Your Email ID</div>
    <label style="top:98px">Zip:</label>
    <div class="input" style="top:92px">Enter Your ZIP Code</div>
    <div class="btn">Sign Up</div>
  </div>
</aside>

<section class="abs panel voices">
  <div class="panel-head">Voices</div>
  <div class="panel-body">
    <article class="voice">
      <div class="thumb" role="img" aria-label="Columnist portrait photo"></div>
      <div class="copy">
        <h3>Cras sollicitudin sodalesique.</h3>
        <div class="by">By Alden Pryce</div>
        <div class="meta">
          <svg width="14" height="12" viewBox="0 0 14 12" aria-hidden="true"><path d="M2 1h10a1 1 0 0 1 1 1v5a1 1 0 0 1-1 1H6l-3 3V8H2a1 1 0 0 1-1-1V2a1 1 0 0 1 1-1z" fill="#eee" stroke="#999"/></svg>
          72 <a href="#">Comment</a> &raquo;
        </div>
      </div>
    </article>
  </div>
</section>

</body>
</html>
```